Designing a brochures for an educational counseling service provider

We would like a 4 sided design on a 11x8.5 paper, half folded. I have including a sample design we did to give you an idea of what we envision but we welcome creativity to make beautiful looking flyers. Text for the flier is included as well as our logo.
- The most important thing is capturing our audience/market. We will be handing these flies to schools, organizations and individual clients.

www.plorvaeducationalconsultants.example

Target Market(s)

We are targeting international students wanting to study in the U.S and Canada.

Industry/Entity Type

Education

Requirements
Must have
• - Clean and clear
• - Our logo should visible and well placed.
• - Could you the pictures of students, libraries and school buildings or you could use the pictures we already have.
Nice to have
• We would like this to match business cards.

```html
<!DOCTYPE html>
<html lang="en">
<head>
<meta charset="utf-8">
<title>Plorva International Educational Consultants – Brochure Cover</title>
<link rel="stylesheet" href="https://fonts.googleapis.com/css2?family=Open+Sans:wght@400;600;700;800&family=Archivo+Black&display=swap">
<style>
  :root {
    --bg: #e4e4e4;
    --paper: #ffffff;
    --ink: #1e1e1e;
    --navy: #1c3d9a;
    --blue: #1f4fb4;
    --orange: #f07d12;
    --green: #6fd23a;
    --green-dark: #3da41f;
    --charcoal-deep: #262626;
    --brand: #1d55b0;
  }
  * { box-sizing: border-box; margin: 0; padding: 0; }
  html, body { width: 1200px; height: 902px; overflow: hidden; }
  body {
    background: var(--bg);
    font-family: "Open Sans", Arial, sans-serif;
    color: var(--ink);
    position: relative;
  }
  .spread {
    position: absolute;
    left: 82px; top: 51px;
    width: 1036px; height: 800px;
    display: flex;
  }
  .panel {
    position: relative;
    width: 518px; height: 800px;
    background: var(--paper);
    overflow: hidden;
  }
  .panel + .panel { border-left: 1px solid #d6d6d6; }
  .panel-shapes { position: absolute; inset: 0; width: 100%; height: 100%; }

  /* Back panel */
  .about-pill {
    position: absolute; left: 50%; top: 58px; transform: translateX(-50%);
    border: 2px solid var(--orange); border-radius: 20px;
    padding: 4px 30px;
    font-family: "Archivo Black", Arial, sans-serif;
    font-size: 17px; color: #fff; letter-spacing: .5px;
  }
  .about-pill .accent { color: var(--orange); }
  .about-text {
    position: absolute; left: 44px; right: 44px; top: 110px;
    color: #f2f2f2; font-size: 12px; line-height: 1.45; text-align: center;
  }
  .about-text p + p { margin-top: 8px; }

  .brand {
    position: absolute; left: 50%; transform: translateX(-50%);
    display: flex; align-items: center; gap: 10px; white-space: nowrap;
  }
  .brand-dot { width: 30px; height: 30px; border-radius: 50%; background: var(--green-dark); flex: none; }
  .brand-name {
    font-family: "Open Sans", Arial, sans-serif; font-weight: 800;
    color: var(--brand); font-size: 15px; line-height: 1.15; text-transform: uppercase;
  }
  .back-brand { top: 505px; }
  .front-brand { top: 42px; }

  .contact {
    position: absolute; left: 0; right: 0; top: 560px; text-align: center;
  }
  .contact-pill {
    display: inline-block; border: 2px solid var(--orange); border-radius: 20px;
    padding: 3px 26px; font-weight: 800; font-size: 18px; color: var(--ink);
  }
  .contact-city { margin-top: 8px; font-weight: 700; font-size: 17px; color: var(--blue); }
  .contact-line { margin-top: 4px; font-weight: 700; font-size: 13px; display: flex; justify-content: center; align-items: center; gap: 6px; }
  .contact-line svg { width: 14px; height: 14px; }
  .social { display: inline-flex; gap: 5px; margin-left: 4px; }
  .social span { width: 18px; height: 18px; border-radius: 50%; background: var(--navy); display: inline-block; }
  .social span + span { background: #2f8fd8; }

  .web-strip {
    position: absolute; left: 0; right: 0; bottom: 18px; text-align: center;
    font-weight: 800; font-size: 14px; color: var(--charcoal-deep);
  }

  /* Front panel */
  .welcome {
    position: absolute; left: 0; right: 0; top: 505px; text-align: center;
    font-family: "Archivo Black", Arial, sans-serif; line-height: 1.1;
  }
  .welcome-kicker { color: #fff; font-size: 22px; }
  .welcome-name { color: var(--orange); font-size: 33px; margin-top: 4px; }
  .welcome-sub { color: #fff; font-size: 20px; margin-top: 4px; }
</style>
</head>
<body>
<main class="spread">

  <section class="panel panel-back">
    <svg class="panel-shapes" viewBox="0 0 518 800">
      <defs>
        <linearGradient id="aboutPhoto" x1="0" y1="0" x2="1" y2="1">
          <stop offset="0" stop-color="#4a4a4a"/>
          <stop offset="1" stop-color="#222"/>
        </linearGradient>
      </defs>
      <g role="img" aria-label="Dimmed photograph of students studying together">
        <path d="M0 0 H518 V380 C380 405 200 440 0 480 Z" fill="url(#aboutPhoto)"/>
      </g>
      <path d="M0 480 C200 440 380 405 518 380 V398 C380 425 200 460 0 502 Z" fill="var(--green)"/>
      <path d="M0 502 C200 460 380 425 518 398 V414 C380 443 200 478 0 522 Z" fill="var(--navy)"/>
      <path d="M0 522 C200 478 380 443 518 414" fill="none" stroke="var(--orange)" stroke-width="5"/>
      <path d="M0 758 C200 750 380 740 518 722 V800 H0 Z" fill="var(--green)"/>
      <path d="M0 749 C200 741 380 731 518 713" fill="none" stroke="var(--orange)" stroke-width="4"/>
    </svg>

    <div class="about-pill">ABOUT <span class="accent">US</span></div>
    <div class="about-text">
      <p>Our mission is to make quality education accessible and affordable to the families we serve. Our services are designed with the child's future in mind. Whether one is seeking an academic or non-academic environment, it is important to us that we set our clients up for success.</p>
      <p>We are a family-centered organization and our goals are the same as those of our clients: for their child to thrive and reach their goals and dreams. With over 10 years of experience in the business, we are aware of the financial obstacles created by the ever increasing cost in education. Our expert consultants work closely with families to map out their educational budget and find the best affordable and quality educational options.</p>
    </div>

    <div class="brand back-brand">
      <span class="brand-dot"></span>
      <span class="brand-name">Plorva International<br>Educational Consultants</span>
    </div>

    <div class="contact">
      <span class="contact-pill">Contact Us</span>
      <div class="contact-city">Westhaven, Texas</div>
      <div class="contact-line">
        <svg viewBox="0 0 16 16"><circle cx="8" cy="8" r="7" fill="none" stroke="var(--orange)" stroke-width="1.6"/><path d="M5.5 4.5 L7 6 L6.2 7.2 C6.8 8.4 7.6 9.2 8.8 9.8 L10 9 L11.5 10.5 L10.6 11.6 C7.5 11.2 4.8 8.5 4.4 5.4 Z" fill="var(--orange)"/></svg>
        +1-555-010-4770
      </div>
      <div class="contact-line">
        <svg viewBox="0 0 16 16"><rect x="2" y="4" width="12" height="8" rx="1" fill="var(--orange)"/><path d="M2.5 4.5 L8 9 L13.5 4.5" fill="none" stroke="#fff" stroke-width="1.2"/></svg>
        info@plorvaeducationalconsultants.example
      </div>
      <div class="contact-line">Follow us on <span class="social"><span></span><span></span></span></div>
    </div>

    <div class="web-strip">www.plorvaeducationalconsultants.example</div>
  </section>

  <section class="panel panel-front">
    <svg class="panel-shapes" viewBox="0 0 518 800">
      <defs>
        <linearGradient id="studentsPhoto" x1="0" y1="0" x2="0" y2="1">
          <stop offset="0" stop-color="#f4f4f4"/>
          <stop offset="0.5" stop-color="#d9a77a"/>
          <stop offset="1" stop-color="#4f6a8f"/>
        </linearGradient>
        <linearGradient id="blueBlock" x1="0" y1="0" x2="1" y2="1">
          <stop offset="0" stop-color="#1a3c9c"/>
          <stop offset="1" stop-color="#2a5fc4"/>
        </linearGradient>
      </defs>
      <path d="M0 200 C160 140 340 115 518 110 V132 C340 135 160 160 0 222 Z" fill="var(--green)"/>
      <g role="img" aria-label="Photograph of five smiling students holding books and folders">
        <ellipse cx="300" cy="310" rx="290" ry="150" fill="url(#studentsPhoto)"/>
      </g>
      <path d="M30 250 C10 330 80 420 220 440 C320 455 440 440 518 405" fill="none" stroke="var(--orange)" stroke-width="12"/>
      <path d="M0 470 C150 450 360 430 518 395 V720 H0 Z" fill="url(#blueBlock)"/>
      <path d="M0 470 C150 450 360 430 518 395" fill="none" stroke="var(--orange)" stroke-width="5"/>
      <rect x="0" y="720" width="518" height="80" fill="var(--green)"/>
      <rect x="0" y="716" width="518" height="4" fill="var(--orange)"/>
    </svg>

    <div class="brand front-brand">
      <span class="brand-dot"></span>
      <span class="brand-name">Plorva International<br>Educational Consultants</span>
    </div>

    <div class="welcome">
      <div class="welcome-kicker">WELCOME TO</div>
      <div class="welcome-name">PLORVA INTERNATIONAL</div>
      <div class="welcome-sub">EDUCATIONAL CONSULTANTS</div>
    </div>

    <div class="web-strip">www.plorvaeducationalconsultants.example</div>
  </section>

</main>
</body>
</html>
```